Business Card Design needed for logo design project

Would like a professional business card for a company involved in financial and latest technologies including CAD design. We would like the card to convey professionalism and communicate that we are involved in up to date technology solutions.

Target Market(s)

Business 2 Business sales

Industry/Entity Type

Financial

Colors

Designer to choose colors to be used in the design.

Requirements
Must have
• Business Name
Logo
Name
Phone
Email
Nice to have
• Website

```html
<!DOCTYPE html>
<html lang="en">
<head>
<meta charset="utf-8">
<title>Vortanel Business Card</title>
<link rel="stylesheet" href="https://fonts.googleapis.com/css2?family=Source+Sans+3:wght@400;600;700&display=swap">
<style>
  :root {
    --backdrop: #e7e5e2;
    --brand-red: #cc1f27;
    --brand-red-deep: #b3181f;
    --band-pink: #e6c8cb;
    --navy: #1d2453;
    --ink: #2b2b2b;
    --white: #ffffff;
  }
  * { box-sizing: border-box; margin: 0; padding: 0; }
  html, body {
    width: 1200px;
    height: 1000px;
    overflow: hidden;
    background: var(--backdrop);
    font-family: "Source Sans 3", "Myriad Pro", sans-serif;
  }
  .stage { position: relative; width: 1200px; height: 1000px; }
  .card {
    position: absolute;
    width: 560px;
    height: 320px;
    overflow: hidden;
    background: linear-gradient(135deg, var(--brand-red-deep) 0%, var(--brand-red) 60%, #d4232b 100%);
    box-shadow: 0 6px 18px rgba(0,0,0,0.15);
  }
  .card-front { left: 80px; top: 160px; }
  .card-back { left: 560px; top: 520px; }

  .wordmark {
    color: var(--white);
    font-weight: 700;
    letter-spacing: 2px;
    line-height: 1;
  }
  .card-front .wordmark {
    position: absolute;
    right: 60px;
    top: 140px;
    font-size: 48px;
  }
  .card-back .wordmark {
    position: absolute;
    left: 40px;
    top: 46px;
    font-size: 28px;
  }

  .info-band {
    position: absolute;
    left: 0;
    right: 0;
    top: 150px;
    height: 140px;
    background: var(--band-pink);
    padding: 28px 40px 0;
  }
  .holder-name {
    color: var(--navy);
    font-size: 32px;
    font-weight: 400;
    line-height: 1;
  }
  .holder-title {
    font-size: 11px;
    color: var(--navy);
    margin-left: 6px;
    vertical-align: middle;
  }
  .contact-lines {
    margin-top: 14px;
    padding-left: 36px;
    font-size: 13px;
    line-height: 1.4;
    color: var(--ink);
  }
  .contact-lines .label {
    color: var(--brand-red);
    font-weight: 600;
  }
  .contact-lines .gap { display: inline-block; width: 12px; }
</style>
</head>
<body>
  <main class="stage">
    <section class="card card-front" aria-label="Card front">
      <div class="wordmark">VORTANEL</div>
    </section>

    <section class="card card-back" aria-label="Card back">
      <div class="wordmark">VORTANEL</div>
      <div class="info-band">
        <h1 class="holder-name">Daniel Reeves<span class="holder-title">CEO</span></h1>
        <p class="contact-lines">
          <span class="label">Address:</span> 42 Harbor Lane Boston, MA 02110<br>
          <span class="label">Phone:</span> + 5550 1928<span class="gap"></span>
          <span class="label">Email:</span> info@vortanel.com<span class="gap"></span>
          <span class="label">Website:</span> vortanel.com
        </p>
      </div>
    </section>
  </main>
</body>
</html>
```